Cedar Hollow Drift Tours

We offer guided cross country ( Nordic ) skiing tours in the National Forest bordering Yellowstone National Park. I need a website that attracts individuals by using photos ( provided by me ) , brief descriptions of what to expect, a place with phone numbers to call for a tour, and I would like the website to feature the same color scheme as the logo, which I will upload.

```html
<!DOCTYPE html>
<html lang="en">
<head>
<meta charset="utf-8">
<title>Cedar Hollow Drift Tours</title>
<link href="https://fonts.googleapis.com/css2?family=Poppins:ital,wght@0,300;0,400;0,500;0,600;0,700;0,800;1,400;1,600&display=swap" rel="stylesheet">
<style>
:root{
  --blue:#2b5ca6;
  --blue-soft:#4a6b9c;
  --navy:#16233d;
  --navy-card:#1c2f4e;
  --grey:#e4e4e4;
  --ink:#1d1d1f;
  --white:#ffffff;
}
*{margin:0;padding:0;box-sizing:border-box}
html,body{width:1200px;height:4184px;overflow:hidden}
body{position:relative;font-family:'Poppins',sans-serif;color:var(--ink);background:var(--white)}
.abs{position:absolute}
.ph{position:absolute;display:block}

/* hero */
.hero{position:absolute;left:0;top:0;width:1200px;height:604px;
  background:radial-gradient(ellipse 520px 300px at 760px 170px,#b77a3e 0%,#7a5434 45%,transparent 75%),
  linear-gradient(180deg,#3d4448 0%,#4a4c4c 40%,#2e3236 100%)}
.hero-shape{position:absolute;left:0;top:0}
.brand-mark{position:absolute;left:122px;top:14px;width:118px;height:118px;border-radius:50%;
  background:var(--white);border:3px solid #c9cfd8;display:flex;align-items:center;justify-content:center;text-align:center;
  font-size:13px;font-weight:600;color:var(--navy);line-height:1.25;padding:12px}
.hero-phone{position:absolute;left:705px;top:12px;font-size:24px;font-weight:500;color:var(--white)}
.btn-touch{position:absolute;left:955px;top:6px;width:132px;height:40px;background:#5f86c9;color:var(--white);
  border-radius:3px;font-size:12px;display:flex;align-items:center;justify-content:center}
.nav{position:absolute;top:64px;font-size:12px;font-weight:500;color:var(--white)}
.hero-title{position:absolute;left:120px;top:282px;font-size:44px;font-weight:800;line-height:46px;color:var(--white);letter-spacing:.5px}
.hero-sub{position:absolute;left:120px;top:430px;width:480px;font-size:12.5px;line-height:20px;color:var(--white);font-weight:500}
.stat{position:absolute;top:284px;color:var(--white)}
.stat small{display:block;font-size:13px;font-weight:400}
.stat b{display:block;font-size:22px;font-weight:600;margin-top:2px}
.thumb{position:absolute;top:354px;height:88px}
.progress{position:absolute;left:628px;top:458px;width:132px;height:4px;background:#4f7fcf}

/* welcome */
.welcome{position:absolute;left:0;top:604px;width:1200px;height:500px;background:var(--grey)}
.h-big{font-weight:800;color:var(--blue);font-size:42px;line-height:1}
.welcome-title{position:absolute;left:588px;top:652px;font-size:46px;font-weight:800;color:#141414}
.welcome-kicker{position:absolute;left:589px;top:705px;font-size:20px;letter-spacing:4.6px;color:#222}
.welcome-text{position:absolute;left:588px;top:755px;width:520px;font-size:14.5px;line-height:29.2px;color:#222}
.btn-read{position:absolute;left:588px;top:937px;width:192px;height:46px;background:var(--blue);color:var(--white);
  font-size:13px;font-weight:500;display:flex;align-items:center;justify-content:center;border-radius:2px}

/* trips */
.trips-title{position:absolute;left:110px;top:1157px}
.trips-sub{position:absolute;left:111px;top:1202px;font-size:17px;color:var(--blue);font-weight:500}
.trip{position:absolute;top:1288px;width:477px;height:335px;border-radius:4px;overflow:hidden;background:var(--navy-card)}
.trip .ph{left:0;top:0;width:477px;height:271px}
.trip-stats{position:absolute;left:0;top:271px;width:477px;height:64px;display:flex}
.trip-stats div{flex:1;text-align:center;color:var(--white);font-size:13px;padding-top:12px;line-height:17px;border-right:1px solid #3b5275}
.trip-stats div:last-child{border-right:none}
.trip-stats span{display:block;color:#3d6fc7;font-size:12px}
.trip-badge{position:absolute;top:1255px;width:86px;height:86px;border-radius:50%;background:var(--white);border:3px solid #2a2a2a;
  display:flex;align-items:center;justify-content:center;text-align:center;font-size:9px;line-height:11px;font-weight:600;color:var(--navy);padding:8px}
.arrow{position:absolute;top:1420px;width:34px;height:34px;border-radius:50%;background:rgba(255,255,255,.85)}

/* gallery */
.kicker{position:absolute;width:1200px;text-align:center;font-size:20px;color:var(--blue-soft);font-weight:400}
.center-title{position:absolute;width:1200px;text-align:center}
.tool{position:absolute;width:44px;height:44px;background:#4e74bb}

/* services */
.service{position:absolute;top:2675px;width:229px;height:297px;border-radius:3px;overflow:hidden;
  background:linear-gradient(180deg,#3e4046 0%,#2c2e33 45%,#17181b 100%)}
.service svg{position:absolute;left:22px;top:50px}
.service h3{position:absolute;left:22px;top:104px;font-size:15px;font-weight:500;color:var(--white)}
.service p{position:absolute;left:22px;top:138px;width:196px;font-size:12.5px;line-height:18px;color:#e6e6e6}

/* testimonial */
.quote-text{position:absolute;left:193px;top:3430px;width:490px;font-size:15.5px;line-height:29.3px;font-style:italic;color:#222}
.quote-name{position:absolute;left:195px;top:3630px;font-size:17px;font-weight:600;font-style:italic;line-height:26px;color:#111}
.photo-frame{position:absolute;left:742px;top:3237px;width:356px;height:412px;background:var(--white);box-shadow:0 4px 14px rgba(0,0,0,.08)}

/* footer */
.footer{position:absolute;left:0;top:3768px;width:1200px;height:416px;background:linear-gradient(180deg,#1c2c4c,#14223d)}
.footer-mark{position:absolute;left:476px;top:3674px;width:240px;height:240px;border-radius:50%;background:var(--white);border:4px solid #2a2a2a;
  display:flex;align-items:center;justify-content:center;text-align:center;font-size:22px;line-height:28px;font-weight:600;color:var(--navy);padding:30px}
.contact{position:absolute;top:3972px;font-size:16px;font-weight:500;color:var(--white);display:flex;align-items:center;gap:10px}
.social{position:absolute;top:4024px;width:34px;height:34px;border-radius:50%;border:1.5px solid var(--white)}
.copy{position:absolute;top:4092px;width:1200px;text-align:center;font-size:15px;color:var(--white)}
.to-top{position:absolute;left:1041px;top:4125px;width:44px;height:44px;background:#4565a5}
</style>
</head>
<body>

<!-- HERO -->
<div class="hero" role="img" aria-label="Sunlit rocky mountain peak above snowy forest at dusk"></div>
<svg class="hero-shape" width="1200" height="604" viewBox="0 0 1200 604">
  <polygon points="0,604 1200,468 1200,528" fill="#262324"/>
  <polygon points="0,604 1200,528 1200,604" fill="#e4e4e4"/>
</svg>
<div class="brand-mark">Cedar Hollow Drift Tours</div>
<div class="hero-phone">(555) 0148-2290-17</div>
<div class="btn-touch">Get In Touch</div>
<div class="nav" style="left:630px">HOME</div>
<div class="nav" style="left:726px">PAGES</div>
<div class="nav" style="left:827px">TREKS</div>
<div class="nav" style="left:924px">BLOG</div>
<div class="nav" style="left:1017px">CONTACTS</div>

<h1 class="hero-title">AMAZING<br>MOUNTAIN TO<br>EXPLORE</h1>
<p class="hero-sub">We offer guided cross country ( Nordic ) skiing tours in the National Forest bordering Yellowstone National Park</p>

<div class="stat" style="left:628px"><small>Tracks</small><b>7</b></div>
<div class="stat" style="left:789px"><small>Altitude</small><b>1650 m</b></div>
<div class="stat" style="left:948px"><small>Tourists / year</small><b>2000 +</b></div>

<div class="thumb ph" style="left:628px;width:132px;background:linear-gradient(180deg,#4a4d52,#2b2d31)" role="img" aria-label="Video preview of a snowy forest trail"></div>
<svg class="abs" style="left:680px;top:384px" width="28" height="28" viewBox="0 0 28 28"><circle cx="14" cy="14" r="12" fill="none" stroke="#fff" stroke-width="2.5"/><polygon points="11,8 20,14 11,20" fill="#fff"/></svg>
<div class="thumb ph" style="left:788px;width:138px;background:linear-gradient(180deg,#3b62b0 0%,#8aa6d3 50%,#e7ebf1 70%,#6f7a88 100%)" role="img" aria-label="Snow-covered mountain under blue sky"></div>
<div class="thumb ph" style="left:948px;width:139px;background:linear-gradient(180deg,#c9d0d8 0%,#aeb8c3 55%,#55606b 75%,#e9edf1 100%)" role="img" aria-label="Snowy valley with evergreen trees"></div>
<div class="progress"></div>

<!-- WELCOME -->
<section class="welcome"></section>
<div class="ph" style="left:117px;top:650px;width:396px;height:393px;border-radius:50%;background:radial-gradient(circle at 55% 65%,#ffffff 0%,#e4e8ef 40%,#a9bde3 75%,#c5d5f0 100%)" role="img" aria-label="Illustration of a cross country skier in front of a snowy mountain and pine tree"></div>
<h2 class="welcome-title">WELCOME TO</h2>
<div class="welcome-kicker">CEDAR HOLLOW DRIFT TOURS</div>
<p class="welcome-text">Lorem Ipsum is simply dummy text of the printing and typesetting industry. Lorem Ipsum has been the industry's standard dummy text ever since the 1500s, when an unknown printer took a galley of type and scrambled it to make a type specimen book. It has survived not only five centuries, but also the leap into electronic typesetting.</p>
<div class="btn-read">READ MORE</div>

<!-- LATEST TRIPS -->
<h2 class="trips-title h-big">LATEST TRIPS</h2>
<div class="trips-sub">EXPLORE THE UNEXPLORED WORLD</div>

<div class="trip" style="left:112px">
  <div class="ph" style="background:linear-gradient(180deg,#2a5db0 0%,#5d86c8 40%,#dfe6ef 65%,#8b96a6 85%,#c7cfd9 100%)" role="img" aria-label="Snowy mountain ridge under a deep blue sky"></div>
  <div class="trip-stats"><div><span>3</span>Days</div><div><span>10</span>Group Size</div><div><span>Easy</span>Difficulty</div></div>
</div>
<div class="trip" style="left:611px">
  <div class="ph" style="background:linear-gradient(180deg,#d4dae2 0%,#9aa6b4 35%,#5a6673 60%,#e6eaee 80%,#3c4651 100%)" role="img" aria-label="Snow-laden pine trees above a mountain valley"></div>
  <div class="trip-stats"><div><span>3</span>Days</div><div><span>5</span>Group Size</div><div><span>Easy</span>Difficulty</div></div>
</div>
<div class="trip-badge" style="left:135px">Cedar Hollow Drift Tours</div>
<div class="trip-badge" style="left:634px">Cedar Hollow Drift Tours</div>
<div class="arrow" style="left:126px"></div><div class="arrow" style="left:538px"></div>
<div class="arrow" style="left:625px"></div><div class="arrow" style="left:1037px"></div>
<svg class="abs" style="left:0;top:0" width="1200" height="1460" viewBox="0 0 1200 1460" fill="none" stroke="#777" stroke-width="1.5">
  <polyline points="145,1433 141,1437 145,1441"/><polyline points="553,1433 557,1437 553,1441"/>
  <polyline points="644,1433 640,1437 644,1441"/><polyline points="1052,1433 1056,1437 1052,1441"/>
</svg>

<!-- GALLERY -->
<div class="kicker" style="top:1686px">GALLERY</div>
<h2 class="center-title h-big" style="top:1714px">PHOTO OF THE DAY!</h2>

<div class="ph" style="left:112px;top:1804px;width:302px;height:200px;background:linear-gradient(180deg,#2b5cb0 0%,#6a8fcb 45%,#e3e8ef 70%,#7e8a9a 100%)" role="img" aria-label="Snow-capped peak under blue sky"></div>
<div class="ph" style="left:114px;top:2036px;width:302px;height:395px;background:linear-gradient(180deg,#7f8d95 0%,#98a3a8 30%,#e0a566 55%,#a5673a 75%,#3c3a3c 100%)" role="img" aria-label="Rocky mountain glowing orange at sunset"></div>
<div class="ph" style="left:450px;top:1806px;width:302px;height:396px;background:linear-gradient(90deg,#233026 0%,#c7d0da 40%,#d9e0e8 60%,#2d3a2f 100%)" role="img" aria-label="Groomed ski trail through tall pine forest"></div>
<div class="tool" style="left:557px;top:1962px"></div><div class="tool" style="left:608px;top:1962px"></div>
<svg class="abs" style="left:557px;top:1962px" width="95" height="44" viewBox="0 0 95 44" fill="none" stroke="#fff" stroke-width="2">
  <rect x="16" y="16" width="12" height="12" rx="3" transform="rotate(45 22 22)"/>
  <circle cx="71" cy="20" r="5"/><line x1="75" y1="24" x2="79" y2="28"/>
</svg>
<div class="ph" style="left:450px;top:2233px;width:302px;height:198px;background:linear-gradient(180deg,#c8d0da 0%,#8e9aa7 35%,#4f5a66 60%,#e3e7ec 80%,#3b4550 100%)" role="img" aria-label="Snowy pines over a mountain valley"></div>
<div class="ph" style="left:788px;top:1804px;width:301px;height:200px;background:linear-gradient(180deg,#b8c0c7 0%,#a7b1ba 55%,#4c5a5f 78%,#e6eaee 100%)" role="img" aria-label="Overcast snowy meadow lined with evergreens"></div>
<div class="ph" style="left:785px;top:2035px;width:302px;height:394px;background:linear-gradient(180deg,#a9bddc 0%,#c7d3e3 45%,#5b6a5e 70%,#dfe5ec 100%)" role="img" aria-label="Snowy conifer forest beneath pale sky"></div>

<!-- SERVICES -->
<div class="kicker" style="top:2551px">TOP SERVICES</div>
<h2 class="center-title h-big" style="top:2580px">WE PROVIDE THE BEST EXPERIENCE</h2>

<div class="service" style="left:112px">
  <svg width="56" height="40" viewBox="0 0 56 40" fill="none" stroke="#fff" stroke-width="2.2"><circle cx="28" cy="10" r="6"/><circle cx="12" cy="14" r="5"/><circle cx="44" cy="14" r="5"/><path d="M16 34c0-8 5-13 12-13s12 5 12 13"/><path d="M2 34c0-6 4-10 10-10M54 34c0-6-4-10-10-10"/></svg>
  <h3>Experienced team</h3>
  <p>Lorem ipsum dolor sit amet, consectetur adipiscing elit, sed do eiusmod tempor incididuno.</p>
</div>
<div class="service" style="left:360px;background:linear-gradient(180deg,#3f3f44 0%,#6b5140 40%,#1c1b1d 100%)">
  <svg width="44" height="44" viewBox="0 0 44 44" fill="#fff"><circle cx="22" cy="6" r="5"/><path d="M18 12h8l4 12h-5l-2 10h-4l2-12-4-4z"/><polygon points="2,42 14,28 22,36 30,28 42,42"/></svg>
  <h3>Expert hikers</h3>
  <p>Lorem ipsum dolor sit amet, consectetur adipiscing elit, sed do eiusmod tempor incididuno.</p>
</div>
<div class="service" style="left:609px">
  <svg width="44" height="44" viewBox="0 0 44 44" fill="none" stroke="#fff" stroke-width="2"><path d="M4 10c8-6 18 0 14 8s-10 12-2 20" stroke-dasharray="3 3"/><line x1="28" y1="26" x2="38" y2="36"/><line x1="38" y1="26" x2="28" y2="36"/></svg>
  <h3>Secret locations</h3>
  <p>Lorem ipsum dolor sit amet, consectetur adipiscing elit, sed do eiusmod tempor incididuno.</p>
</div>
<div class="service" style="left:857px;background:linear-gradient(180deg,#5a5e66 0%,#3a3d44 45%,#17181b 100%)">
  <svg width="48" height="48" viewBox="0 0 48 48" fill="none" stroke="#fff" stroke-width="3"><line x1="24" y1="2" x2="24" y2="46"/><line x1="5" y1="13" x2="43" y2="35"/><line x1="43" y1="13" x2="5" y2="35"/><polyline points="18,6 24,11 30,6"/><polyline points="18,42 24,37 30,42"/></svg>
  <h3>Great Snow</h3>
  <p>Lorem ipsum dolor sit amet, consectetur adipiscing elit, sed do eiusmod tempor incididuno.</p>
</div>

<!-- TESTIMONIALS -->
<div class="kicker" style="top:3094px">TESTIMONIALS</div>
<h2 class="center-title h-big" style="top:3128px">WHAT OUR VISITORS SAY</h2>
<svg class="abs" style="left:0;top:3280px" width="1200" height="488" viewBox="0 0 1200 488"><polygon points="0,82 1200,9 1200,488 0,488" fill="#e4e4e4"/></svg>

<svg class="abs" style="left:119px;top:3415px" width="54" height="44" viewBox="0 0 54 44" fill="#b9b9b9"><path d="M0 44V26C0 10 8 2 22 0v8c-7 2-10 6-10 12h10v24zM30 44V26C30 10 38 2 52 0v8c-7 2-10 6-10 12h10v24z"/></svg>
<p class="quote-text">Lorem Ipsum is simply dummy text of the printing and typesetting industry. Lorem Ipsum has been the industry's standard dummy text ever since the 1500s, when an unknown printer took a galley of type and scrambled it to make a type specimen book. It has survived not only five centuries, but also the leap into electronic typesetting.</p>
<div class="quote-name">Dana Whitfield<br>(Marketing Manager)</div>
<svg class="abs" style="left:523px;top:3613px" width="54" height="44" viewBox="0 0 54 44" fill="#b9b9b9"><path d="M54 0v18c0 16-8 24-22 26v-8c7-2 10-6 10-12H32V0zM24 0v18c0 16-8 24-22 26v-8c7-2 10-6 10-12H2V0z"/></svg>

<div class="photo-frame"></div>
<div class="ph" style="left:757px;top:3253px;width:326px;height:378px;background:linear-gradient(180deg,#d9d3cf 0%,#c7c2c1 45%,#b57a3a 65%,#6d5240 100%)" role="img" aria-label="Hiker in an orange jacket sitting with a backpack on a mountain top"></div>

<!-- FOOTER -->
<footer class="footer" role="img" aria-label="Dark blue snowy forest backdrop"></footer>
<div class="footer-mark">Cedar Hollow Drift Tours</div>

<div class="contact" style="left:375px">
  <svg width="20" height="20" viewBox="0 0 20 20"><rect width="20" height="20" rx="4" fill="#fff"/><path d="M6 4l2 3-1.5 1.5a8 8 0 0 0 5 5L13 12l3 2-1 2.5c-5 0-11-6-11-11z" fill="#1c2c4c"/></svg>
  <span>(555) 0148-2290-17</span>
</div>
<div class="contact" style="left:604px">
  <svg width="20" height="20" viewBox="0 0 20 20"><polygon points="1,10 19,2 13,19 10,12" fill="#fff"/></svg>
  <span>hello@cedarhollowdrift.test</span>
</div>

<div class="social" style="left:503px"></div>
<div class="social" style="left:550px"></div>
<div class="social" style="left:597px"></div>
<div class="social" style="left:643px"></div>

<p class="copy">Copyright © 2021 <b style="font-weight:600">Cedar Hollow Drift Tours</b>. All rights reserved</p>
<div class="to-top"></div>
<svg class="abs" style="left:1041px;top:4125px" width="44" height="44" viewBox="0 0 44 44" fill="none" stroke="#9fb6e0" stroke-width="2"><polyline points="13,26 22,17 31,26"/></svg>

</body>
</html>
```